A clean crisp business card for a Landscape Construction company. Designed to be easy to read contact/ info and also be appealing/interesting, unlike a traditional business card.

Industry/Entity Type

Landscape Construction

Contact Information for Business Card

Company name : Bramblecrest Landscape Construction, phone number: (877) 62Vales, website:Bramblecrestlandscapes.example, Email, sales@bramblecrestlandscapes.example

Requirements
Nice to have
• Luxurious finishes/ details…. Icons or emblems next to contact info
Should not have
• Clipart or general pictures

```html
<!DOCTYPE html>
<html lang="en">
<head>
<meta charset="utf-8">
<title>Bramblecrest Landscape Construction – Business Card</title>
<link rel="stylesheet" href="https://fonts.googleapis.com/css2?family=Cinzel:wght@500&family=Montserrat:wght@400;500;800&display=swap">
<style>
  :root {
    --brand-blue: #2169ad;
    --deep-blue: #1b5a9c;
    --leaf-green: #8cc63f;
    --paper: #f3f3f3;
    --ink: #1f1f1f;
    --backdrop: #e4e4e4;
  }
  * { margin: 0; padding: 0; box-sizing: border-box; }
  html, body { width: 1200px; height: 1149px; overflow: hidden; }
  body {
    background: var(--backdrop);
    font-family: "Montserrat", Arial, sans-serif;
    position: relative;
  }
  .card {
    position: absolute;
    left: 170px;
    width: 860px;
    height: 491px;
    overflow: hidden;
    box-shadow: 0 10px 30px rgba(0,0,0,0.18);
  }
  /* Front side */
  .card-front { top: 60px; background: var(--brand-blue); }
  .front-mark {
    position: absolute; left: 0; right: 0; top: 170px;
    display: flex; align-items: center; justify-content: center; gap: 18px;
  }
  .mark-dot { width: 22px; height: 22px; border-radius: 50%; background: var(--leaf-green); }
  .front-name {
    font-family: "Cinzel", "Times New Roman", serif;
    font-weight: 500; font-size: 38px; color: #ffffff; letter-spacing: 1px;
    text-align: center; line-height: 1.15;
  }
  .front-web {
    position: absolute; left: 0; right: 0; top: 360px;
    display: flex; align-items: center; justify-content: center; gap: 26px;
  }
  .front-rule { width: 160px; height: 2px; background: var(--leaf-green); }
  .front-url { font-size: 19px; font-weight: 500; color: #ffffff; letter-spacing: 0.5px; white-space: nowrap; }
  .front-url .accent { color: var(--leaf-green); }

  /* Back side */
  .card-back { top: 598px; background: var(--paper); }
  .back-mark {
    position: absolute; left: 50px; top: 100px; width: 320px;
    display: flex; align-items: center; gap: 12px;
  }
  .back-mark .mark-dot { flex: none; width: 16px; height: 16px; }
  .back-name {
    font-family: "Cinzel", "Times New Roman", serif;
    font-weight: 500; font-size: 25px; color: var(--brand-blue); line-height: 1.2;
  }
  .band-block { position: absolute; left: 0; top: 300px; width: 310px; height: 191px; background: var(--brand-blue); }
  .band-accent { position: absolute; left: 70px; top: 300px; width: 240px; height: 22px; background: var(--leaf-green); }
  .band-base { position: absolute; left: 0; bottom: 0; width: 100%; height: 72px; background: var(--brand-blue); }
  .contact {
    position: absolute; left: 420px; top: 110px; width: 410px;
  }
  .person-name { font-weight: 800; font-size: 30px; color: var(--deep-blue); }
  .person-role { font-weight: 400; font-size: 20px; color: var(--ink); margin-top: 4px; }
  .contact-rule { width: 230px; height: 2px; background: var(--leaf-green); margin: 28px 0 22px; }
  .contact-list { list-style: none; }
  .contact-item {
    display: flex; align-items: center; gap: 12px;
    font-size: 17px; color: var(--ink); margin-bottom: 12px; white-space: nowrap;
  }
  .contact-icon { width: 24px; height: 24px; flex: none; }
</style>
</head>
<body>

<section class="card card-front" aria-label="Business card front">
  <div class="front-mark">
    <span class="mark-dot"></span>
    <div class="front-name">Bramblecrest<br>Landscape Construction</div>
  </div>
  <div class="front-web">
    <span class="front-rule"></span>
    <span class="front-url">www.<span class="accent">bramblecrestlandscapes</span>.example</span>
    <span class="front-rule"></span>
  </div>
</section>

<section class="card card-back" aria-label="Business card back">
  <div class="back-mark">
    <span class="mark-dot"></span>
    <div class="back-name">Bramblecrest<br>Landscape Construction</div>
  </div>
  <div class="band-block"></div>
  <div class="band-accent"></div>
  <div class="band-base"></div>

  <div class="contact">
    <div class="person-name">Marcus Ellery</div>
    <div class="person-role">Managing Director</div>
    <div class="contact-rule"></div>
    <ul class="contact-list">
      <li class="contact-item">
        <svg class="contact-icon" viewBox="0 0 24 24" aria-hidden="true">
          <circle cx="12" cy="12" r="12" fill="#1b5a9c"/>
          <path d="M8.5 6.5l2 2.2-1.2 1.4c.8 1.7 2 2.9 3.6 3.7l1.4-1.2 2.2 2-1.2 1.9c-4-.5-7.6-4.1-8-8z" fill="#fff"/>
        </svg>
        (877) 62Vales
      </li>
      <li class="contact-item">
        <svg class="contact-icon" viewBox="0 0 24 24" aria-hidden="true">
          <circle cx="12" cy="12" r="12" fill="#1b5a9c"/>
          <rect x="6" y="8" width="12" height="8" fill="none" stroke="#fff" stroke-width="1.4"/>
          <path d="M6 8l6 5 6-5" fill="none" stroke="#fff" stroke-width="1.4"/>
        </svg>
        sales@bramblecrestlandscapes.example
      </li>
      <li class="contact-item">
        <svg class="contact-icon" viewBox="0 0 24 24" aria-hidden="true">
          <circle cx="12" cy="12" r="12" fill="#8cc63f"/>
          <circle cx="12" cy="12" r="6" fill="none" stroke="#fff" stroke-width="1.3"/>
          <ellipse cx="12" cy="12" rx="2.6" ry="6" fill="none" stroke="#fff" stroke-width="1.2"/>
          <path d="M6 12h12" stroke="#fff" stroke-width="1.2"/>
        </svg>
        www.bramblecrestlandscapes.example
      </li>
    </ul>
  </div>
</section>

</body>
</html>
```